Business card and company stationary - Corvane Cleaning Ltd

1. Who are we and who are our customers?

o We are a relatively new cleaning company, established December 2008. We are a small company. We have 24 staff and we offer domestic and commercial cleaning services.
o We both (me and my wife) have been working for many years in the cleaning industry. We worked for some of the biggest and best cleaning companies in UK. We’ve been operatives, supervisors and managers.
o Inevitably after so many years of working for someone else, we decided to start our own business.
o Our domestic customers are middle class families and busy professionals. We’ve got some commercial customers, mainly offices.
o We are growing steadily.

2. What do we do? What are our services?

o Cleaning. We’ve got range of services - not to many but still can be daunting and confusing for some.
o Generally we’ve got domestic and commercial clients. The approach to the domestic cleaning customers is different to the commercial. In the way we want to say that it is cleaning that we do, but we acknowledge the environment and we appreciate the personal circumstances and requirements that are present. We do care, we listen and we try to work out the best possible way to complete our work.
o Mainly we get our work through referrals

3. What do we want with our stationery ?

o To place and maintain our message and reach out to people and organisations
o We want to advertise, communicate and sale.
o We are going to sell services.
o Increase membership, loyalty and support.

We are after business card design, headed letter and compliment slip.
We would like the headed letter to be created in formats suitable for :
- printing format
- also for use in our daily correspondence via e mail with clients and staff in a easy to edit and write format

The website we have is still under contraction and the domain is corvanecleaning.example

Target Market(s)

Families, individuals, businesses.

Industry/Entity Type

Cleaning Service

Contact Information for Business Card

FRONT :
Company Name - Corvane Cleaning Ltd
Company address - 41 Pelbury Rd, Pelbury, Essex, RM14 7QT
Name - Mrs. Teodora Vasilkova - Tedi
Title - Managing Director
Company phone - 020 8837 2591
E mail - tedi.vasilkova@corvanecleaning.example

BACK :

Company website - corvanecleaning.example
E mail - enquiries@corvanecleaning.example

Font styles to use
Serif

Requirements
Must have
• The above items and company logo...maybe at the back. But I'm free for any suggestions.

```html
<!DOCTYPE html>
<html lang="en">
<head>
<meta charset="utf-8">
<title>Corvane Cleaning Ltd – Letterhead</title>
<link href="https://fonts.googleapis.com/css2?family=Arimo:wght@400;700&family=Jost:wght@300;400&display=swap" rel="stylesheet">
<style>
  :root {
    --backdrop: #1e2833;
    --paper: #ffffff;
    --ink: #111111;
    --muted: #444444;
    --accent: #33c4f0;
    --signature-tone: #e6e9ec;
  }
  * { margin: 0; padding: 0; box-sizing: border-box; }
  html, body { width: 1000px; height: 1200px; overflow: hidden; }
  body { background: var(--backdrop); position: relative; }

  .letterhead {
    position: absolute; left: 157px; top: 116px;
    width: 685px; height: 967px;
    background: var(--paper);
    font-family: "Arimo", Arial, sans-serif;
    color: var(--ink);
  }

  .brand { position: absolute; right: 62px; top: 42px; width: 220px; height: 140px; }
  .brand-mark {
    position: absolute; right: 22px; top: 4px;
    width: 90px; height: 90px; border-radius: 50%;
    border: 4px solid var(--ink);
  }
  .brand-name {
    position: absolute; right: 0; top: 108px;
    font-family: "Arimo", Arial, sans-serif; font-weight: 700;
    font-size: 17px; color: var(--ink); white-space: nowrap;
  }

  .letter {
    position: absolute; left: 190px; top: 276px; width: 434px;
    font-size: 14px; line-height: 16.5px;
  }
  .letter p { margin-bottom: 16.5px; text-align: justify; hyphens: auto; -webkit-hyphens: auto; }
  .letter .date { margin-bottom: 16px; }
  .letter .recipient { margin-bottom: 33px; text-align: left; }
  .letter .salutation { margin-bottom: 17px; }
  .letter .closing { margin-top: 33px; margin-bottom: 0; }
  .signature {
    width: 150px; height: 60px; margin: 2px 0 0 -26px;
    background: linear-gradient(90deg, var(--signature-tone), #f4f6f7);
    border-radius: 4px;
  }
  .signatory { margin-top: 5px; }

  .contact-list { position: absolute; left: 28px; top: 588px; width: 107px; list-style: none; }
  .contact-item { height: 62px; }
  .contact-item.is-web { height: 72px; }
  .contact-tab {
    height: 24px; background: var(--accent);
    border-radius: 12px 0 0 12px; position: relative;
  }
  .contact-tab svg { position: absolute; left: 11px; top: 5px; width: 14px; height: 14px; }
  .contact-text {
    font-family: "Jost", sans-serif; font-weight: 300;
    font-size: 13px; line-height: 15px; color: var(--muted);
    text-align: right; padding-right: 6px; margin-top: 6px; white-space: nowrap;
  }
  .contact-text.web { font-size: 11.5px; line-height: 13px; }

  .legal {
    position: absolute; right: 64px; top: 925px;
    font-size: 9px; color: var(--ink); white-space: nowrap;
  }
</style>
</head>
<body>
<main class="letterhead">
  <div class="brand">
    <span class="brand-mark"></span>
    <span class="brand-name">Corvane Cleaning Ltd</span>
  </div>

  <section class="letter">
    <p class="date">June 16, 2016</p>
    <p class="recipient">First Last Name<br>Street Address<br>City, State 00000</p>
    <p class="salutation">Dear :</p>
    <p>Lorem ipsum dolor sit amet, consectetur adipiscing elit. Aenean ut ipsum eget massa hendrerit vestibulum vel in velit. Donec pretium neque velit.</p>
    <p>Aliquam porta lectus nec mauris ornare venenatis. Vivamus non est turpis, et cursus sem. Mauris vehicula erat in diam auctor at bibendum nisl lacinia.</p>
    <p>Morbi imperdiet neque vehicula nunc convallis gravida. Vestibulum iaculis pretium placerat. Integer consequat, est sit amet facilisis eleifend, nibh nibh varius orci, eget dapibus arcu dui non purus. Pellentesque in magna mauris. Duis enim sapien, dictum vitae condimentum a, pulvinar vel lacus. Mauris et molestie nibh. Vestibulum vitae nulla at metus elementum porta sit amet interdum elit. Nulla sollicitudin neque eu nulla volutpat congue.</p>
    <p class="closing">Sincerely,</p>
    <div class="signature" role="img" aria-label="Handwritten signature"></div>
    <p class="signatory">Admin</p>
  </section>

  <ul class="contact-list">
    <li class="contact-item">
      <div class="contact-tab"><svg viewBox="0 0 24 24"><path fill="#111" d="M6.6 10.8a15 15 0 0 0 6.6 6.6l2.2-2.2c.3-.3.7-.4 1-.2 1.1.4 2.3.6 3.6.6.6 0 1 .4 1 1V20c0 .6-.4 1-1 1A17 17 0 0 1 3 4c0-.6.4-1 1-1h3.5c.6 0 1 .4 1 1 0 1.3.2 2.5.6 3.6.1.3 0 .7-.2 1z"/></svg></div>
      <p class="contact-text">088 8888 888</p>
    </li>
    <li class="contact-item">
      <div class="contact-tab"><svg viewBox="0 0 24 24"><circle cx="12" cy="12" r="4" fill="none" stroke="#111" stroke-width="2.6"/><path d="M16 8v5.5a2.5 2.5 0 0 0 5 0V12a9 9 0 1 0-3.5 7.1" fill="none" stroke="#111" stroke-width="2.6"/></svg></div>
      <p class="contact-text">name@email.com</p>
    </li>
    <li class="contact-item is-web">
      <div class="contact-tab"><svg viewBox="0 0 24 24"><circle cx="12" cy="12" r="10" fill="#111"/><path d="M2 12h20M12 2c3 3 3 17 0 20M12 2c-3 3-3 17 0 20M4 7h16M4 17h16" fill="none" stroke="#33c4f0" stroke-width="1.4"/></svg></div>
      <p class="contact-text web">www.corvanecleaning<br>.example</p>
    </li>
    <li class="contact-item">
      <div class="contact-tab"><svg viewBox="0 0 24 24"><path fill="#111" d="M12 3 2 12h3v9h5v-6h4v6h5v-9h3z"/></svg></div>
      <p class="contact-text">Address, Adress<br>80000</p>
    </li>
  </ul>

  <p class="legal">Company No: 00000 &nbsp;| VAT : 000000000</p>
</main>
</body>
</html>
```